Create professional business cards using the attached logo previously designed using BrightPitch. Would like to see a business card that stands out from the crowd.

One side should just have our logo and our business name ie Lamppost Guidance Partners, and the other side should have a smaller version of logo and company name, but together with our business details detailed below. Two cards will need to be produced for myself and my business partner

Professional financial advice to streetlighting engineers and finance people.

Business

The business card will need to contain; name, title (ie Director, email, mobile number, and website address.

• HoratioB and HoratioM

• We would like modern clean looking professional business cards that incorprates the attached .ai file logo. Font used is HoratioB and HoratioM and the name of the company is Lamppost Guidance Partners.
• One side should just have our logo and our business name ie Lamppost Guidance Partners, and the other side should have a smaller version of logo and company name, but together with our business details as above.
• We would potentially like to emboss the logo and name Lamppost Guidance Partners Ltd. Perhaps something that reflects the transition from night to day eg white on one side, black on the other.
• We are open minded. Do not want anything that would appear as a stock copy and paste from a 'normal' business card website eg CardMorrow

```html
<!DOCTYPE html>
<html lang="en">
<head>
<meta charset="utf-8">
<title>Lamppost Guidance Partners – Business Cards</title>
<link rel="stylesheet" href="https://fonts.googleapis.com/css2?family=Questrial&family=Roboto+Condensed:wght@700&display=swap">
<style>
  :root {
    --canvas: #d4d5d7;
    --card: #ffffff;
    --ink: #111111;
    --ring: #9a9b9e;
    --night: #0c0c10;
    --violet: #6b4aa8;
    --magenta: #d6266f;
    --sky: #4f7fc4;
    --amber: #f5a623;
  }
  * { box-sizing: border-box; margin: 0; padding: 0; }
  html, body { width: 1200px; height: 1000px; overflow: hidden; }
  body { background: var(--canvas); position: relative; font-family: "Questrial", "Century Gothic", sans-serif; color: var(--ink); }

  .card { position: absolute; left: 279px; width: 672px; height: 393px; background: var(--card); overflow: hidden; }
  .card--first { top: 87px; }
  .card--second { top: 516px; }

  .card__art { position: absolute; inset: 0; width: 672px; height: 393px; }

  .brand { position: absolute; left: 36px; top: 42px; display: flex; align-items: center; gap: 18px; }
  .brand__mark { width: 40px; height: 40px; border-radius: 50%; background: var(--violet); flex: none; }
  .brand__name { font-family: "Roboto Condensed", "Arial Narrow", sans-serif; font-weight: 700; font-size: 30px; line-height: 32px; letter-spacing: 0.3px; text-transform: uppercase; color: var(--ink); }

  .person { position: absolute; left: 81px; top: 166px; }
  .person__name { font-size: 31px; line-height: 38px; }
  .person__creds { font-size: 18px; line-height: 24px; margin-top: 2px; padding-left: 2px; }

  .contact { position: absolute; top: 308px; font-size: 19px; line-height: 28px; }
  .contact--phone { left: 79px; }
  .contact--web { left: 287px; }
  .contact__row { display: flex; align-items: center; gap: 14px; }
  .contact__icon { width: 23px; height: 23px; flex: none; }
</style>
</head>
<body>

<section class="card card--first">
  <svg class="card__art" viewBox="0 0 672 393" role="img" aria-label="Decorative bulb-shaped panel of glowing coloured light stripes and tiles on black">
    <defs>
      <linearGradient id="glow1" x1="0" y1="0" x2="1" y2="1">
        <stop offset="0" stop-color="#2a1240"/>
        <stop offset="0.35" stop-color="#7a3f9e"/>
        <stop offset="0.6" stop-color="#c8336f"/>
        <stop offset="0.85" stop-color="#4f6fb8"/>
        <stop offset="1" stop-color="#16161e"/>
      </linearGradient>
    </defs>
    <path d="M 392 0 C 366 40, 362 150, 392 212 C 422 268, 494 288, 574 304 C 626 314, 656 346, 672 388 L 672 0 Z" fill="var(--ring)"/>
    <path d="M 402 0 C 376 40, 372 150, 402 208 C 432 262, 502 282, 580 297 C 632 308, 660 340, 672 372 L 672 0 Z" fill="url(#glow1)"/>
  </svg>
  <div class="brand">
    <span class="brand__mark"></span>
    <div class="brand__name">Lamppost Guidance<br>Partners</div>
  </div>
  <div class="person">
    <div class="person__name">Dr Felix Marlowe</div>
    <div class="person__creds">MA(Cantab) DPhil FCA</div>
  </div>
  <div class="contact contact--phone">
    <div class="contact__row">
      <svg class="contact__icon" viewBox="0 0 24 24" fill="none" stroke="currentColor" stroke-width="1.4"><circle cx="12" cy="12" r="11"/><rect x="8.5" y="5.5" width="7" height="13" rx="1.5"/><line x1="10.5" y1="16" x2="13.5" y2="16"/></svg>
      <span>07480 215964</span>
    </div>
  </div>
  <div class="contact contact--web">
    <div class="contact__row">
      <svg class="contact__icon" viewBox="0 0 24 24" fill="none" stroke="currentColor" stroke-width="1.4"><circle cx="12" cy="12" r="11"/><rect x="6" y="8" width="12" height="8.5"/><polyline points="6,8 12,13 18,8"/></svg>
      <span>felix@lamppostguidance.org</span>
    </div>
    <div class="contact__row">
      <svg class="contact__icon" viewBox="0 0 24 24" fill="none" stroke="currentColor" stroke-width="1.4"><circle cx="12" cy="12" r="11"/><circle cx="12" cy="12" r="6.5"/><ellipse cx="12" cy="12" rx="2.8" ry="6.5"/><line x1="5.5" y1="12" x2="18.5" y2="12"/></svg>
      <span>www.lamppostguidance.org</span>
    </div>
  </div>
</section>

<section class="card card--second">
  <svg class="card__art" viewBox="0 0 672 393" role="img" aria-label="Decorative bulb-shaped panel of glowing coloured light stripes and tiles on black">
    <defs>
      <linearGradient id="glow2" x1="0" y1="0" x2="1" y2="1">
        <stop offset="0" stop-color="#2a1240"/>
        <stop offset="0.35" stop-color="#7a3f9e"/>
        <stop offset="0.6" stop-color="#c8336f"/>
        <stop offset="0.85" stop-color="#4f6fb8"/>
        <stop offset="1" stop-color="#16161e"/>
      </linearGradient>
    </defs>
    <path d="M 392 0 C 366 40, 362 150, 392 212 C 422 268, 494 288, 574 304 C 626 314, 656 346, 672 388 L 672 0 Z" fill="var(--ring)"/>
    <path d="M 402 0 C 376 40, 372 150, 402 208 C 432 262, 502 282, 580 297 C 632 308, 660 340, 672 372 L 672 0 Z" fill="url(#glow2)"/>
  </svg>
  <div class="brand">
    <span class="brand__mark"></span>
    <div class="brand__name">Lamppost Guidance<br>Partners</div>
  </div>
  <div class="person">
    <div class="person__name">Rowan Ashby</div>
    <div class="person__creds">CEng BSc (Hons) MIET MILP</div>
  </div>
  <div class="contact contact--phone">
    <div class="contact__row">
      <svg class="contact__icon" viewBox="0 0 24 24" fill="none" stroke="currentColor" stroke-width="1.4"><circle cx="12" cy="12" r="11"/><rect x="8.5" y="5.5" width="7" height="13" rx="1.5"/><line x1="10.5" y1="16" x2="13.5" y2="16"/></svg>
      <span>07722 608451</span>
    </div>
  </div>
  <div class="contact contact--web">
    <div class="contact__row">
      <svg class="contact__icon" viewBox="0 0 24 24" fill="none" stroke="currentColor" stroke-width="1.4"><circle cx="12" cy="12" r="11"/><rect x="6" y="8" width="12" height="8.5"/><polyline points="6,8 12,13 18,8"/></svg>
      <span>rowan@lamppostguidance.org</span>
    </div>
    <div class="contact__row">
      <svg class="contact__icon" viewBox="0 0 24 24" fill="none" stroke="currentColor" stroke-width="1.4"><circle cx="12" cy="12" r="11"/><circle cx="12" cy="12" r="6.5"/><ellipse cx="12" cy="12" rx="2.8" ry="6.5"/><line x1="5.5" y1="12" x2="18.5" y2="12"/></svg>
      <span>www.lamppostguidance.org</span>
    </div>
  </div>
</section>

</body>
</html>
```